New Website Design for High Quality Sailing School

This client has revised it's logo and branding and wants to create a new website that delivers a high-quality compelling design. Please read the brief, wireframes, brand guidelines and logos really carefully before you start your design work.
Note that the winning designer, based on the homepage, will be expected to do the other internal page designs as a part of this project.

Target Market(s)

Mainly Young Adults (20-35), High Net Worth, Love Sailing and Adventures

Industry/Entity Type

Leisure

Number of Pages Required

5+ page

Font styles to use
Sans Serif
Other font styles liked:
• Hyperspace Race

Requirements
Must have
• Attention to detail, high quality designs, applying the new branding carefully, and clean as per the brief.
Nice to have
• Keep it simple, but use the imagery. Take a look at the sites they like.
Should not have
• Inconsistency in design theme

```html
<!DOCTYPE html>
<html lang="en">
<head>
<meta charset="utf-8">
<title>Meridian Sailing — Home</title>
<link rel="stylesheet" href="https://fonts.googleapis.com/css2?family=Orbitron:wght@600;700;800&family=Exo+2:wght@400;500&display=swap">
<style>
  :root{
    --ink:#231f20;
    --orange:#ff3b1f;
    --card:#434245;
    --white:#ffffff;
    --muted:#c9c7c8;
    --grey-btn:#67666a;
    --menu:#d2d2d2;
  }
  *{margin:0;padding:0;box-sizing:border-box}
  html,body{width:1200px;height:2611px;overflow:hidden;background:var(--ink)}
  body{position:relative;font-family:"Exo 2",sans-serif;color:var(--white)}
  .abs{position:absolute}
  .display{font-family:"Orbitron",sans-serif;font-weight:700;letter-spacing:.04em;text-transform:uppercase}
  .btn{position:absolute;display:flex;align-items:center;justify-content:center;border-radius:4px;
       background:var(--orange);color:var(--white);font-family:"Exo 2",sans-serif;font-size:14px;font-weight:500;letter-spacing:.04em;text-transform:uppercase}
  .btn--grey{background:var(--grey-btn)}

  .site-nav{left:0;top:0;width:1200px;height:94px;background:var(--ink);z-index:3}
  .brand{left:90px;top:24px;display:flex;align-items:center;gap:10px}
  .brand-mark{width:34px;height:34px;border-radius:50%;background:var(--orange)}
  .brand-name{font-family:"Exo 2",sans-serif;font-size:16px;font-weight:500;letter-spacing:.16em;line-height:1.1}
  .brand-name small{display:block;font-size:10px;letter-spacing:.3em}
  .nav-links{left:464px;top:40px;display:flex;gap:23px;font-size:14px;letter-spacing:.02em}
  .nav-links .active{color:var(--orange)}
  .nav-cta{left:999px;top:29px;width:113px;height:35px}

  .dropdown{left:430px;top:94px;width:166px;height:136px;background:var(--menu);opacity:.92;border-radius:0 0 4px 4px;z-index:4;
            padding:12px 0 0 38px;font-size:12px;line-height:23px;color:#555;letter-spacing:.03em}
  .dropdown .current{color:var(--orange)}

  .hero{left:0;top:94px;width:1200px;height:584px;background:linear-gradient(160deg,#6d6d6d 0%,#3c3c3c 35%,#2b2b2b 70%,#505050 100%)}
  .hero-title{left:83px;top:250px;font-size:40px;line-height:54px;font-weight:800;z-index:2}
  .hero-sub{left:83px;top:418px;width:390px;height:55px;background:rgba(190,190,190,.55);color:var(--ink);
            font-size:20px;display:flex;align-items:center;justify-content:center;z-index:2}
  .hero-cta{left:83px;top:494px;width:113px;height:35px;z-index:2}
  .play{left:553px;top:290px;z-index:2}

  .stakes-title{left:0;width:1200px;top:756px;text-align:center;font-size:34px}
  .stakes-sub{left:0;width:1200px;top:848px;text-align:center;font-size:15px;line-height:20px;letter-spacing:.06em}
  .card{top:919px;width:321px;height:190px;background:var(--card);font-size:16.5px;line-height:20px;letter-spacing:.03em;padding:58px 30px 0 32px}
  .card--accent{background:var(--orange);box-shadow:3px 3px 6px rgba(0,0,0,.4)}

  .courses-title{left:0;width:1200px;top:1180px;text-align:center;font-size:34px}

  .photo{background:linear-gradient(180deg,#9a9a9a,#4a4a4a)}
  .feature-frame{left:0;top:1285px;width:572px;height:355px;background:var(--orange)}
  .feature-h{font-size:15px;letter-spacing:.05em}
  .feature-p{font-size:16.5px;line-height:20px;color:var(--muted);letter-spacing:.02em}
  .rule{height:2px;width:62px;background:var(--orange)}

  .review-links{left:593px;top:2388px;display:flex;gap:22px;font-size:14px;color:var(--muted)}
  .review-link{display:flex;align-items:center;gap:8px}
  .review-link i{width:44px;height:44px;border-radius:50%;background:var(--grey-btn);display:block}
</style>
</head>
<body>

<header class="site-nav abs">
  <div class="brand abs"><span class="brand-mark"></span><span class="brand-name">MERIDIAN<small>SAILING</small></span></div>
  <nav class="nav-links abs">
    <span class="active">Destinations ⌄</span><span>Liveaboard Courses</span><span>Our Tribe</span><span>Online Masterclasses</span>
  </nav>
  <a class="btn nav-cta">Email now</a>
</header>

<div class="dropdown abs">
  <div class="current">Mexico</div><div>Grenadines</div><div>Bahamas</div><div>Croatia</div><div>Custom Trips</div>
</div>

<section>
  <div class="hero abs" role="img" aria-label="Black-and-white photo of waves washing over a dark sand beach"></div>
  <h1 class="hero-title abs display">Embark on a<br>lifetime of<br>adventures</h1>
  <div class="hero-sub abs display">Learn to sail in a week</div>
  <a class="btn hero-cta">Email now</a>
  <svg class="play abs" width="96" height="96" viewBox="0 0 96 96" aria-label="Play video">
    <circle cx="48" cy="48" r="47" fill="#8a8a8a" opacity=".8"/>
    <path d="M27 19 L80 48 L27 77 Z" fill="#ff3b1f"/>
  </svg>
</section>

<section>
  <h2 class="stakes-title abs display">The stakes are high</h2>
  <p class="stakes-sub abs display">Sailing can be<br>daunting, expensive, overwhelming...</p>
  <div class="card card--accent abs" style="left:58px">Gain the skills, experience and formal certifications to successfully embark on your sailing journey</div>
  <div class="card abs" style="left:431px">You deserve an incredible adventure, award-winning instructors, sexy new sailboats and a fun learning environment</div>
  <div class="card abs" style="left:804px;padding-left:38px">Enjoy sailing adventures with friends and family in exotic destinations</div>
</section>

<section>
  <h2 class="courses-title abs display">The ultimate liveboard sailing courses</h2>

  <div class="feature-frame abs"></div>
  <div class="photo abs" style="left:0;top:1273px;width:552px;height:347px" role="img" aria-label="Black-and-white photo of a catamaran at sea under a cloudy sky"></div>
  <h3 class="feature-h abs display" style="left:595px;top:1375px">300&nbsp; Alumni sailing the oceans of the world</h3>
  <div class="rule abs" style="left:595px;top:1405px"></div>
  <p class="feature-p abs" style="left:595px;top:1428px;width:330px">Here at Meridian, we help thousands of people turn their sailing dreams into a reality</p>
  <a class="btn abs" style="left:592px;top:1507px;width:113px;height:35px">Learn more</a>

  <h3 class="feature-h abs display" style="left:223px;top:1833px">Outstanding instructors</h3>
  <p class="feature-p abs" style="left:223px;top:1883px;width:390px">Award-winning instructors, educators first and foremost, not just great sailors!</p>
  <a class="btn btn--grey abs" style="left:223px;top:1946px;width:113px;height:35px">Learn more</a>
  <div class="photo abs" style="left:641px;top:1732px;width:559px;height:347px;background:linear-gradient(180deg,#d8d8d8,#6e6e6e)" role="img" aria-label="Black-and-white photo of an instructor on the deck of a sailboat"></div>

  <div class="photo abs" style="left:0;top:2170px;width:552px;height:347px;background:linear-gradient(135deg,#cfcfcf,#3a3a3a)" role="img" aria-label="Black-and-white photo of hands holding a tablet showing charts"></div>
  <h3 class="feature-h abs display" style="left:590px;top:2259px">Outstanding reviews</h3>
  <p class="feature-p abs" style="left:590px;top:2312px;width:390px">We are the highest-rated NCSA Sailing-School. Check some of the reviews TripNotes.</p>
  <div class="review-links abs">
    <span class="review-link"><i></i>TripNotes</span>
    <span class="review-link"><i></i>SocialBook</span>
  </div>
</section>

</body>
</html>
```